Trvmlegal.com needs a wedsite. Law Office of Darnell P. Whitby

Darnell P. Whitby is a criminal law firm that is 5 years old. We have already had all the content written and now just need the website designed. We also just finished our logo design using Pixel Harbor and would like it used in the design of the website.

Industry/Entity Type

Law Firm

Number of Pages Required

5+ page

Requirements
Must have
• I was our new logo to be on the website also. I want Dallas sites as the stock pictures for the website. For example the Grey Stone Tribunal. I also need to be able to add YouTube videos. It has to adjust to be seen on computers and also cell phones. I need to be able to have a information sheet for clients to fill out and submit back to me.

```html
<!DOCTYPE html>
<html lang="en">
<head>
<meta charset="utf-8">
<title>Law Office of Darnell P. Whitby</title>
<link rel="stylesheet" href="https://fonts.googleapis.com/css2?family=Open+Sans:wght@400;600&family=Raleway:wght@400;500&family=Roboto+Slab:wght@400;700&display=swap">
<style>
:root{
  --navy:#0d2f6b;
  --nav-bg:#dcdcdc;
  --text:#444;
  --band:#f2f2f2;
  --line:#cfcfcf;
  --footer:#1d1d1d;
  --white:#fff;
  --slab:"Roboto Slab",Georgia,serif;
}
*{box-sizing:border-box;margin:0;padding:0}
html,body{width:894px;height:1200px;overflow:hidden;background:var(--white)}
body{position:relative;font-family:"Open Sans",sans-serif;color:var(--text)}
.abs{position:absolute}
.line{display:block;white-space:nowrap}

/* navigation */
.nav{left:0;top:0;width:894px;height:45px;background:var(--nav-bg)}
.nav a{position:absolute;top:17px;font-size:9px;color:#333;text-decoration:none}
.brand{left:417px;top:1px;width:88px;height:88px;border-radius:50%;background:var(--navy);border:4px solid #e8e8e8;display:flex;align-items:center;justify-content:center;text-align:center;padding:10px;color:var(--white);font-weight:600;font-size:8px;line-height:1.25;z-index:2}

/* hero */
.hero{left:0;top:45px;width:894px;height:423px;background:linear-gradient(90deg,#6e4a3c 0%,#8a4a33 35%,#7c4533 65%,#5f4a44 100%)}
.hero-person{left:120px;top:140px;width:220px;height:328px;background:linear-gradient(180deg,#3b3b3f,#1c1c20)}
.hero-title{left:350px;top:166px;font-family:var(--slab);font-weight:700;font-size:42px;line-height:1.1;color:var(--white)}
.hero-text{left:350px;top:225px;font-size:9px;line-height:17px;font-weight:600;color:var(--white)}
.btn-light{left:351px;top:291px;width:78px;height:25px;background:var(--white);color:var(--navy);font-family:var(--slab);font-size:10px;display:flex;align-items:center;justify-content:center;border-radius:2px}

/* about */
.about-title{left:138px;top:513px;font-family:var(--slab);font-weight:400;font-size:26px;line-height:1.2;color:var(--navy)}
.about-sub{left:137px;top:554px;font-family:var(--slab);font-size:13.5px;color:#444}
.about-text{left:137px;top:582px;font-size:8.5px;line-height:16.9px;color:#555}
.btn-navy{left:136px;top:723px;width:68px;height:24px;background:var(--navy);color:var(--white);font-size:8.5px;display:flex;align-items:center;justify-content:center;gap:5px;border-radius:2px}
.video{left:507px;top:519px;width:249px;height:207px;background:linear-gradient(180deg,#8a7250 0%,#c49a55 60%,#a8793b 100%)}
.video-bar{left:0;top:0;width:249px;height:25px;background:rgba(0,0,0,.55);color:var(--white);font-size:8.5px;padding:6px 8px}
.video-controls{left:0;bottom:0;width:249px;height:11px;background:#1a1a1a}

/* band */
.band{left:0;top:774px;width:894px;height:310px;background:var(--band)}
.h2{font-family:var(--slab);font-weight:400;font-size:17.5px;color:var(--navy)}
.h2-rule{height:1px;background:#bbb}
.svc{left:137px;width:178px;height:30px;border-bottom:1px solid var(--line);font-family:var(--slab);font-size:9.5px;color:#444;display:flex;align-items:center;gap:5px;white-space:nowrap}
.team-photo{left:349px;width:89px;height:54px;background:linear-gradient(135deg,#6b5a52,#2f2c2e)}
.team-name{left:446px;font-family:var(--slab);font-size:9.5px;color:#222;white-space:nowrap}
.team-role{left:447px;font-family:var(--slab);font-size:8px;color:#777}

.contact-box{left:567px;top:795px;width:188px;height:273px;background:var(--navy);border-radius:4px;padding:7px}
.contact-inner{width:100%;height:100%;background:var(--white);border-radius:3px;position:relative}
.contact-inner h3{font-family:"Raleway",sans-serif;font-weight:500;font-size:17px;color:var(--navy);text-align:center;padding-top:10px;height:36px;border-bottom:1px solid #ddd}
.field-label{left:12px;font-family:"Raleway",sans-serif;font-size:8px;color:#666}
.field{left:12px;width:149px;height:19px;border:1px solid #ccc}
.btn-quote{left:15px;top:233px;width:144px;height:20px;background:var(--navy);color:var(--white);border-radius:4px;font-family:"Raleway",sans-serif;font-size:10px;display:flex;align-items:center;justify-content:center}

/* footer */
.footer{left:0;top:1084px;width:894px;height:116px;background:var(--footer);color:var(--white)}
.f-head{font-size:11px;font-weight:600}
.f-item{font-size:8.3px;color:#eee;display:flex;align-items:flex-start;gap:5px;line-height:14px;white-space:nowrap}
.social-sq{width:25px;height:20px;background:var(--white)}
.social-label{font-size:10px;color:#ccc}
</style>
</head>
<body>

<nav class="abs nav">
  <a style="left:210px">Home</a>
  <a style="left:265px">Attornet Profile</a>
  <a style="left:354px">History</a>
  <a style="left:531px">How We can help</a>
  <a style="left:631px">Service</a>
  <a style="left:690px">Contact Us</a>
</nav>
<div class="abs brand">Law Office of Darnell P. Whitby</div>

<section class="abs hero" role="img" aria-label="Red brick stone tribunal building with towers"></section>
<div class="abs hero-person" role="img" aria-label="Attorney in a dark suit and tie"></div>
<h1 class="abs hero-title">Best Lawyers</h1>
<p class="abs hero-text">
  <span class="line">The point of using Lorem Ipsum is that it has a more-or-less normal</span>
  <span class="line">distribution of letters, as opposed to using 'Content here,</span>
  <span class="line">content here', making it look like readable English. Many &nbsp;sites still in</span>
</p>
<div class="abs btn-light">Know More</div>

<h2 class="abs about-title">About Our Attorney Profiles</h2>
<p class="abs about-sub">Our Aggressive Criminal Defense Team Fights for You</p>
<p class="abs about-text">
  <span class="line">You are innocent unless proven guilty. But our criminal justice system often unjustly</span>
  <span class="line">denies this fundamental constitutional right. The Law Office of Darnell P. Whitby seeks</span>
  <span class="line">to balance the scales of justice.</span>
  <span class="line">Our Dallas-Fort Worth law firm solely handles criminal defense cases so we can dedicate</span>
  <span class="line">our full resources to the pursuit of justice. Our criminal defense attorneys presume that</span>
  <span class="line">every case we take will go to trial and aggressively advocate for you from the moment we</span>
  <span class="line">take your case. Because the wheels of justice spin 24 hours, so do we. If you are arrested</span>
  <span class="line">after-hours, on weekends or on holidays, we are available to handle your jail release.</span>
</p>
<div class="abs btn-navy">Read More
  <svg width="9" height="6" viewBox="0 0 9 6"><path d="M0 3h7M5 .5 8 3 5 5.5" stroke="#fff" stroke-width="1.2" fill="none"/></svg>
</div>
<div class="abs video" role="img" aria-label="Video of a courtroom scene with attorneys and a judge">
  <div class="abs video-bar">Lorem Ipsum is simply dummy text
    <svg style="position:absolute;right:10px;top:8px" width="9" height="9" viewBox="0 0 9 9"><circle cx="7" cy="1.5" r="1.5" fill="#fff"/><circle cx="1.5" cy="4.5" r="1.5" fill="#fff"/><circle cx="7" cy="7.5" r="1.5" fill="#fff"/><path d="M7 1.5 1.5 4.5 7 7.5" stroke="#fff" fill="none"/></svg>
  </div>
  <div class="abs video-controls">
    <div class="abs" style="left:44px;top:4px;width:146px;height:2px;background:#444"></div>
    <div class="abs" style="left:44px;top:4px;width:73px;height:2px;background:#d22"></div>
    <div class="abs" style="left:214px;top:4px;width:22px;height:2px;background:#ddd"></div>
  </div>
</div>

<section class="abs band"></section>

<h2 class="abs h2" style="left:138px;top:797px">Our Services</h2>
<div class="abs h2-rule" style="left:137px;top:820px;width:143px"></div>
<div class="abs svc" style="top:824px"><span>»</span>Murder &amp; Other Homicide Offenses</div>
<div class="abs svc" style="top:854px"><span>»</span>Sexual Offenses</div>
<div class="abs svc" style="top:884px"><span>»</span>Expungements &amp; Non-Disclosures</div>
<div class="abs svc" style="top:914px"><span>»</span>Early Probation Release</div>
<div class="abs svc" style="top:944px"><span>»</span>Probation Violations</div>
<div class="abs svc" style="top:974px"><span>»</span>Other Violent Offenses</div>
<div class="abs svc" style="top:1004px"><span>»</span>Drug Offenses</div>

<h2 class="abs h2" style="left:350px;top:797px">Our Team</h2>
<div class="abs h2-rule" style="left:350px;top:820px;width:143px"></div>
<div class="abs team-photo" style="top:836px" role="img" aria-label="Portrait of Darnell P. Whitby"></div>
<div class="abs team-name" style="top:845px">Darnell P. Whitby</div>
<div class="abs team-role" style="top:862px">Chriminal Lawyer</div>
<div class="abs team-photo" style="top:899px" role="img" aria-label="Portrait of Marisol Quenby-Hart"></div>
<div class="abs team-name" style="top:908px">Marisol Quenby-Hart</div>
<div class="abs team-role" style="top:925px">Chriminal Lawyer</div>
<div class="abs team-photo" style="top:963px;background:linear-gradient(135deg,#f4f4f4,#8fb5d8)" role="img" aria-label="Portrait of Tobias Renwick"></div>
<div class="abs team-name" style="top:972px">Tobias Renwick</div>
<div class="abs team-role" style="top:989px">Chriminal Lawyer</div>

<div class="abs contact-box">
  <form class="contact-inner">
    <h3>Contact Us</h3>
    <div class="abs field-label" style="top:42px">Name</div>
    <div class="abs field" style="top:54px"></div>
    <div class="abs field-label" style="top:79px">Email</div>
    <div class="abs field" style="top:91px"></div>
    <div class="abs field-label" style="top:115px">Phone</div>
    <div class="abs field" style="top:127px"></div>
    <div class="abs field-label" style="top:151px">Comment</div>
    <div class="abs field" style="top:163px;height:45px"></div>
    <div class="abs btn-quote">Request For quote</div>
  </form>
</div>

<footer class="abs footer">
  <div class="abs f-head" style="left:137px;top:14px">Contact Us</div>
  <div class="abs f-item" style="left:137px;top:34px">
    <svg width="7" height="10" viewBox="0 0 7 10" style="margin-top:2px;flex:none"><path d="M3.5 0a3.5 3.5 0 0 0-3.5 3.5C0 6 3.5 10 3.5 10S7 6 7 3.5A3.5 3.5 0 0 0 3.5 0z" fill="#fff"/><circle cx="3.5" cy="3.5" r="1.2" fill="#1d1d1d"/></svg>
    <span>2145 Elmwood Lane Suite 300<br>Harbor Row dallas tx 75201</span></div>
  <div class="abs f-item" style="left:137px;top:70px">
    <svg width="9" height="9" viewBox="0 0 9 9" style="margin-top:2px"><path d="M2 0 3.5 2.5 2.3 3.6a6 6 0 0 0 3 3L6.5 5.5 9 7 8 9C3.5 9 0 5.5 0 1z" fill="#fff"/></svg>
    <span>123 456 7890</span></div>
  <div class="abs f-item" style="left:137px;top:88px">
    <svg width="9" height="7" viewBox="0 0 9 7" style="margin-top:3px"><rect width="9" height="7" fill="#fff"/><path d="M0 0 4.5 4 9 0" stroke="#1d1d1d" fill="none"/></svg>
    <span>info@trvmlegal.com</span></div>

  <div class="abs f-head" style="left:296px;top:12px">Our service</div>
  <div class="abs" style="left:296px;top:33px">
    <div class="f-item" style="margin-bottom:3px">» Murder &amp; Other Homicide Offenses</div>
    <div class="f-item" style="margin-bottom:3px">» Sexual Offenses</div>
    <div class="f-item" style="margin-bottom:3px">» Expungements &amp; Non-Disclosures</div>
    <div class="f-item">» Early Probation Release</div>
  </div>
  <div class="abs" style="left:467px;top:33px">
    <div class="f-item" style="margin-bottom:3px">» Probation Violations</div>
    <div class="f-item" style="margin-bottom:3px">» Other Violent Offenses</div>
    <div class="f-item" style="margin-bottom:3px">» DWI, DUI</div>
    <div class="f-item">» Drug Offenses</div>
  </div>

  <div class="abs f-head" style="left:616px;top:12px">Follow Us</div>
  <div class="abs social-sq" style="left:616px;top:38px"></div>
  <div class="abs social-label" style="left:647px;top:40px">Friendwall</div>
  <div class="abs social-sq" style="left:616px;top:72px"></div>
  <div class="abs social-label" style="left:647px;top:74px">Chirpline</div>
</footer>

</body>
</html>
```